Heater product information sheets

I need the two product information sheets organized and laid out in a clean, easy to read attractive manner. These sheets are to advertise propane heaters for outdoor use and for wholesale to propane distributors, restaurants and homeowners that need to have propane heat as the winter ends and spring begins. They will be used for chilly evenings when people want to be outside eating, drinking and being social.
Updates

Low design quality

Target Market(s)

Restaurants, hospitality industry, special events, party rental companies, home owners with backyards

Font styles to use
Sans Serif

Requirements
Must have
• My logo in the document instead of k. Dahlby and company
Nice to have
• I would like to see Fire illustrated coming up the heaters and on the round glass, show it up the middle of the glass tube propane heater.

```html
<!DOCTYPE html>
<html lang="en">
<head>
<meta charset="utf-8">
<title>Outdoor Propane Heater</title>
<link href="https://fonts.googleapis.com/css2?family=Montserrat:wght@600;700;800;900&family=Open+Sans:wght@400;600;700&display=swap" rel="stylesheet">
<style>
:root{
  --orange:#f26b1d;
  --orange-deep:#d9530f;
  --orange-light:#f79a52;
  --ink:#1b1b1b;
  --white:#ffffff;
  --paper:#ffffff;
  --steel-dark:#1c1c1c;
  --steel-mid:#5c5c5c;
}
*{margin:0;padding:0;box-sizing:border-box}
html,body{width:898px;height:1200px;overflow:hidden;background:var(--paper)}
body{font-family:"Open Sans",Arial,sans-serif;color:var(--ink);position:relative}
.sheet{position:relative;width:898px;height:1200px;overflow:hidden}

.title{position:absolute;left:62px;top:112px;font-family:"Montserrat",Arial,sans-serif;font-weight:900;font-size:64px;line-height:70px;letter-spacing:.5px;color:var(--ink)}

.offers{position:absolute;left:480px;top:118px;list-style:none;width:380px}
.offers li{display:flex;align-items:flex-start;gap:14px;margin-bottom:22px;font-family:"Montserrat",Arial,sans-serif;font-weight:800;font-size:21px;line-height:25px;text-transform:uppercase;color:var(--ink)}
.offers .check{flex:0 0 28px;height:28px;margin-top:-1px}

.scenery{position:absolute;left:0;top:430px;width:898px;height:595px;background:linear-gradient(135deg,var(--orange-light) 0%,var(--orange) 45%,var(--orange-deep) 100%)}

.heater{position:absolute;left:130px;top:372px;width:250px;height:660px;border-radius:14px;background:linear-gradient(90deg,var(--steel-dark) 0%,var(--steel-mid) 45%,var(--steel-dark) 100%)}

.specs{position:absolute;left:468px;top:452px;width:400px;color:var(--white)}
.specs h2{font-family:"Montserrat",Arial,sans-serif;font-weight:800;font-size:25px;letter-spacing:.5px;padding-bottom:6px;margin-bottom:10px;border-bottom:2px solid rgba(255,255,255,.7);display:inline-block}
.specs ul{list-style:none;margin-bottom:22px}
.specs li{position:relative;padding-left:16px;font-size:15px;line-height:21px;margin-bottom:3px;font-weight:600}
.specs li::before{content:"";position:absolute;left:2px;top:8px;width:6px;height:6px;background:var(--white);border-radius:50%}

.note{position:absolute;left:62px;top:1044px;display:flex;gap:18px;align-items:flex-start}
.note .label{background:var(--ink);color:var(--white);font-family:"Montserrat",Arial,sans-serif;font-weight:800;font-size:20px;padding:4px 16px}
.note p{font-size:15px;line-height:20px;color:var(--ink)}

.cta{position:absolute;left:440px;top:1100px;width:458px;height:36px;background:var(--orange);color:var(--white);font-family:"Montserrat",Arial,sans-serif;font-weight:800;font-size:20px;line-height:36px;padding-left:18px;letter-spacing:.5px}

.contact{position:absolute;left:458px;top:1140px;font-size:14px;line-height:19px;color:var(--ink)}
.contact .company{font-weight:700}
.contact .row{display:flex;align-items:center;gap:6px}
.contact .row span + svg{margin-left:8px}
.contact svg{width:13px;height:13px;flex:0 0 13px}
</style>
</head>
<body>
<div class="sheet">

  <h1 class="title">OUTDOOR<br>PROPANE<br>HEATER</h1>

  <ul class="offers">
    <li><svg class="check" viewBox="0 0 28 28"><circle cx="14" cy="14" r="13" fill="var(--orange)"/><path d="M8 14.5l4 4 8-9" fill="none" stroke="#fff" stroke-width="3" stroke-linecap="round" stroke-linejoin="round"/></svg><span>Rentals for<br>live events</span></li>
    <li><svg class="check" viewBox="0 0 28 28"><circle cx="14" cy="14" r="13" fill="var(--orange)"/><path d="M8 14.5l4 4 8-9" fill="none" stroke="#fff" stroke-width="3" stroke-linecap="round" stroke-linejoin="round"/></svg><span>Rentals for<br>restaurants &amp;<br>catering halls</span></li>
    <li><svg class="check" viewBox="0 0 28 28"><circle cx="14" cy="14" r="13" fill="var(--orange)"/><path d="M8 14.5l4 4 8-9" fill="none" stroke="#fff" stroke-width="3" stroke-linecap="round" stroke-linejoin="round"/></svg><span>Purchase for<br>your home or<br>business</span></li>
  </ul>

  <div class="scenery" role="img" aria-label="Blurred autumn trees outdoors with a warm orange tint"></div>

  <div class="heater" role="img" aria-label="Photo of a black outdoor propane patio heater with a round reflector top"></div>

  <section class="specs">
    <h2>SPECIFICATIONS</h2>
    <ul>
      <li>Powerful 46,000 BTU</li>
      <li>Black Powder Coated Finish</li>
      <li>Uses 20 lb. Propane Tank</li>
      <li>CE, CB, AGA, CSA, with ETL certificate and ROHS approved</li>
    </ul>
    <h2>ADDITIONAL DETAILS</h2>
    <ul>
      <li>Commercial Quality</li>
      <li>For Outdoor Use Only</li>
      <li>Conforms to ANSI STD Z83.26-2014 Certified to CSA STD 2.37-2014 Gas-fired outdoor infrared patio heaters</li>
      <li>Safety Auto Shut Off Switch</li>
      <li>Thermostatic Control</li>
      <li>Base Diameter 17", Anti-Tilt Design</li>
      <li>Standard Wheels - Easy to Move</li>
      <li>Run time: 8-10 hours with standard 20 lb. Propane tank 88" Tall</li>
      <li>Heating Area: 200 sq. ft.</li>
    </ul>
  </section>

  <div class="note">
    <span class="label">NOTE</span>
    <p>Price: Starting at $250 each<br>Assembly &amp; Delivery available upon request<br>Discounts for large quantity orders</p>
  </div>

  <div class="cta">TO RENT OR PURCHASE</div>

  <div class="contact">
    <div class="company">K. Dahlby &amp; Company</div>
    <div class="row">
      <svg viewBox="0 0 14 14"><path d="M3 1l2.5 3-1.5 1.5c.8 1.8 2.2 3.2 4 4L9.5 8l3 2.5-1.5 2.5C6 13 1 8 1 3z" fill="var(--orange)"/></svg><span>973-555-0148</span>
      <svg viewBox="0 0 14 14"><rect x="1" y="3" width="12" height="8" rx="1" fill="var(--orange)"/><path d="M1.5 3.5L7 8l5.5-4.5" fill="none" stroke="#fff" stroke-width="1.2"/></svg><span>Mark@KDeventrental.com</span>
    </div>
    <div class="row">
      <svg viewBox="0 0 14 14"><path d="M7 1a4 4 0 0 1 4 4c0 3-4 8-4 8S3 8 3 5a4 4 0 0 1 4-4z" fill="var(--orange)"/><circle cx="7" cy="5" r="1.5" fill="#fff"/></svg><span>42 Maple Ave Clifton, NJ 07011</span>
    </div>
  </div>

</div>
</body>
</html>
```